Event Graphic for Free Community Event

We need a graphic created for a community event that is aimed at families with younger children called Tots Jamboree. This is a free event and has a fair/carnival feel to it with rides, games, and food. I need the graphic to be flexible enough to be able to be modified and used in a variety of ways on different print and digital marketing materials. I also need the centerpiece of the design to be an event logo that can be used as a standalone element.

The overall feel needs to be fun and friendly with a slightly modern edge to it. Attached are some images used in past events. These are for reference only and do not need to be simulated or used in the final product.

Target Market(s)

Families with children

Industry/Entity Type

Church

Font styles to use
Sans Serif

Requirements
Must have
• - Logo that incorporates the event name
- Event Date: September 19 2020
- Event Time: 10am - 2pm
- Church name and logo incorporated: Bright Harbor Community Church (see attached logo files)
Nice to have
• - Bright colors
- Flexible design elements that are interchangeable and scalable for use of the design in different layouts across different mediums and materials.
Should not have
• - Any references or images related to drugs, alcohol, tobacco, or other subjects that would be inappropriate for children.

```html
<!DOCTYPE html>
<html lang="en">
<head>
<meta charset="utf-8">
<title>Tots Jamboree 2020 — Flyer</title>
<link href="https://fonts.googleapis.com/css2?family=Fredoka:wght@400;600;700&family=Nunito:wght@800&family=Oswald:wght@400&family=Raleway:wght@400;500;700&family=Open+Sans:ital,wght@1,400&display=swap" rel="stylesheet">
<style>
  :root {
    --orange: #f5921e;
    --blue: #0a9fe8;
    --pink: #ef3f8c;
    --date-pink: #e8227a;
    --yellow: #f7c51e;
    --navy: #1d3e5c;
    --white: #ffffff;
    --page: #f4f4f4;
    --sky-top: #7cc6f2;
    --sky-low: #cfe9f8;
    --grass: #5fae3a;
  }
  html, body {
    margin: 0;
    width: 1200px;
    height: 1200px;
    overflow: hidden;
    background: var(--page);
  }
  .flyer {
    position: absolute;
    left: 187px;
    top: 66px;
    width: 1032px;
    height: 1336px;
    background: var(--white);
    transform: scale(0.8);
    transform-origin: 0 0;
    overflow: hidden;
  }
  .flyer-shapes { position: absolute; inset: 0; }
  .abs { position: absolute; margin: 0; }

  .church {
    left: 105px; top: 460px;
    display: flex; align-items: center; gap: 16px;
  }
  .church-mark {
    width: 76px; height: 76px; border-radius: 50%;
    border: 3px solid var(--white); box-sizing: border-box;
  }
  .church-name {
    font-family: "Nunito", sans-serif; font-weight: 800;
    color: var(--white); font-size: 31px; line-height: 1.1;
  }
  .event-title {
    left: 112px; top: 560px;
    font-family: "Fredoka", sans-serif; font-weight: 700;
    color: var(--white); line-height: 0.95;
  }
  .event-title .line-1 { display: block; font-size: 140px; }
  .event-title .line-2 { display: block; font-size: 90px; letter-spacing: -1px; }
  .event-year {
    left: 394px; top: 858px; width: 144px; text-align: center;
    font-family: "Oswald", sans-serif; font-size: 64px; color: var(--white);
  }

  .date { left: 92px; top: 1000px; text-align: center; width: 180px; }
  .label {
    font-family: "Raleway", sans-serif; font-weight: 500; font-size: 33px;
    display: flex; align-items: center; justify-content: center; gap: 6px;
  }
  .date .label { color: var(--date-pink); padding-left: 34px; }
  .date-day {
    font-family: "Raleway", sans-serif; font-weight: 700;
    font-size: 38px; color: var(--date-pink); margin-top: 6px;
  }
  .date-year {
    font-family: "Raleway", sans-serif; font-weight: 400;
    font-size: 68px; line-height: 0.9; color: var(--date-pink);
  }
  .divider {
    left: 296px; top: 1005px; width: 3px; height: 148px; background: var(--navy);
  }
  .time { left: 318px; top: 1000px; width: 260px; }
  .time .label { color: var(--navy); padding-left: 44px; }
  .time-range {
    display: flex; align-items: flex-start; white-space: nowrap; margin-top: 24px;
    font-family: "Raleway", sans-serif; color: var(--navy);
  }
  .time-range .hour { font-weight: 700; font-size: 72px; line-height: 0.85; }
  .time-range .sub {
    display: flex; flex-direction: column; font-size: 26px; line-height: 1.05;
    font-weight: 500; padding-left: 2px;
  }

  .attractions {
    right: 50px; top: 828px; text-align: right; color: var(--white);
  }
  .attractions-kicker {
    font-family: "Fredoka", sans-serif; font-weight: 400;
    font-size: 56px; line-height: 1; padding-right: 4px;
  }
  .attractions-title {
    margin: 0;
    font-family: "Fredoka", sans-serif; font-weight: 600;
    font-size: 60px; line-height: 1;
  }
  .attractions-rule {
    width: 178px; height: 3px; background: var(--white);
    margin: 10px 0 14px auto;
  }
  .attractions-list {
    list-style: none; margin: 0; padding: 0;
    font-family: "Raleway", sans-serif; font-size: 35px; line-height: 50px;
  }
  .attractions-list li::after { content: " •"; font-size: 28px; padding-left: 6px; }

  .tagline {
    left: 0; right: 0; top: 1268px; text-align: center;
    font-family: "Open Sans", sans-serif; font-style: italic;
    font-size: 28px; color: var(--white); letter-spacing: 0.5px;
  }
</style>
</head>
<body>
<main class="flyer">
  <svg class="flyer-shapes" viewBox="0 0 1032 1336" width="1032" height="1336">
    <defs>
      <linearGradient id="photo-tone" x1="0" y1="0" x2="0" y2="1">
        <stop offset="0" stop-color="#7cc6f2"/>
        <stop offset="0.45" stop-color="#cfe9f8"/>
        <stop offset="0.75" stop-color="#e89aa8"/>
        <stop offset="1" stop-color="#5fae3a"/>
      </linearGradient>
      <linearGradient id="grass-tone" x1="0" y1="0" x2="0" y2="1">
        <stop offset="0" stop-color="#b9c9a0"/>
        <stop offset="1" stop-color="#5fae3a"/>
      </linearGradient>
      <clipPath id="spot-clip"><circle cx="793" cy="570" r="116"/></clipPath>
    </defs>

    <rect class="event-photo" x="0" y="0" width="1032" height="560" fill="url(#photo-tone)" role="img" aria-label="Photo of children running across a grassy field under a blue sky"/>
    <g clip-path="url(#spot-clip)">
      <rect x="677" y="450" width="232" height="200" fill="url(#grass-tone)" role="img" aria-label="Photo detail of children running on green grass"/>
      <rect x="677" y="650" width="232" height="40" fill="var(--blue)"/>
    </g>

    <path class="corner-orange" fill="var(--orange)" d="M0 0 H280 C250 60 240 170 140 222 C90 246 35 240 0 252 Z"/>
    <path class="corner-pink" fill="var(--pink)" d="M835 0 H1032 V285 C990 292 925 272 912 222 C900 172 962 150 942 108 C920 66 852 42 835 0 Z"/>
    <path class="corner-orange-small" fill="var(--orange)" d="M1032 215 V285 C1010 290 990 286 985 270 C1000 250 1020 240 1032 215 Z"/>

    <path class="title-blob-shadow" fill="var(--yellow)" transform="translate(24 10)" d="M0 300 C60 288 100 330 130 380 C170 440 220 446 280 440 C360 432 420 420 480 410 C560 398 640 392 650 440 C660 500 600 530 562 540 C512 552 508 600 518 660 C530 740 520 800 480 830 C400 890 280 925 200 938 C120 950 60 985 0 995 Z"/>
    <path class="title-blob" fill="var(--blue)" d="M0 300 C60 288 100 330 130 380 C170 440 220 446 280 440 C360 432 420 420 480 410 C560 398 640 392 650 440 C660 500 600 530 562 540 C512 552 508 600 518 660 C530 740 520 800 480 830 C400 890 280 925 200 938 C120 950 60 985 0 995 Z"/>
    <ellipse fill="var(--white)" cx="-10" cy="665" rx="52" ry="135"/>
    <circle class="year-badge" fill="var(--blue)" cx="466" cy="898" r="72"/>

    <circle class="attractions-blob" fill="var(--orange)" cx="850" cy="1085" r="310"/>
    <g class="footer-band" fill="var(--orange)">
      <rect x="0" y="1258" width="1032" height="78"/>
      <ellipse cx="70" cy="1290" rx="95" ry="72"/>
      <ellipse cx="250" cy="1290" rx="95" ry="72"/>
      <ellipse cx="420" cy="1290" rx="95" ry="72"/>
      <ellipse cx="590" cy="1290" rx="95" ry="72"/>
    </g>

    <g class="icon-calendar" fill="none" stroke="var(--date-pink)" stroke-width="2.5">
      <rect x="127" y="1007" width="24" height="22" rx="2"/>
      <line x1="127" y1="1014" x2="151" y2="1014"/>
      <line x1="133" y1="1003" x2="133" y2="1009"/>
      <line x1="145" y1="1003" x2="145" y2="1009"/>
    </g>
    <g class="icon-clock" fill="none" stroke="var(--navy)" stroke-width="2.5">
      <circle cx="384" cy="1020" r="15"/>
      <polyline points="377,1020 382,1026 392,1013"/>
    </g>
  </svg>

  <div class="abs church">
    <span class="church-mark"></span>
    <span class="church-name">Bright Harbor<br>Community Church</span>
  </div>

  <h1 class="abs event-title">
    <span class="line-1">Tots</span>
    <span class="line-2">Jamboree</span>
  </h1>
  <div class="abs event-year">2020</div>

  <div class="abs date">
    <div class="label">DATE</div>
    <div class="date-day">19,SEPT</div>
    <div class="date-year">2020</div>
  </div>
  <div class="abs divider"></div>
  <div class="abs time">
    <div class="label">TIME</div>
    <div class="time-range">
      <span class="hour">10</span>
      <span class="sub"><span>:00</span><span>AM</span></span>
      <span class="hour">–2</span>
      <span class="sub"><span>:00</span><span>PM</span></span>
    </div>
  </div>

  <section class="abs attractions">
    <div class="attractions-kicker">fun</div>
    <h2 class="attractions-title">Attractions</h2>
    <div class="attractions-rule"></div>
    <ul class="attractions-list">
      <li>Free Food</li>
      <li>Bungee Jump</li>
      <li>Rock wall</li>
      <li>Inflatables Rides</li>
      <li>and many more...</li>
    </ul>
  </section>

  <p class="abs tagline">....come one, come all and lets have fun</p>
</main>
</body>
</html>
```